BKA

Please send us some options for letterhead I attached our Logo. In addition to the Logo we need this information somewhere on the page

47 Fenbury Lane
Hollisford, CT 06412
203-481-7629

```html
<!DOCTYPE html>
<html lang="en">
<head>
<meta charset="utf-8">
<title>BKA Letterhead</title>
<link rel="stylesheet" href="https://fonts.googleapis.com/css2?family=Arimo:wght@400;500&display=swap">
<style>
  :root {
    --backdrop: #ececec;
    --paper: #ffffff;
    --ink: #1a1a1a;
    --brand-dark: #4a4140;
    --brand-blue: #0a76ba;
    --rule-grey: #d9dcdf;
  }
  * { margin: 0; padding: 0; box-sizing: border-box; }
  html, body {
    width: 1000px;
    height: 1200px;
    overflow: hidden;
    background: var(--backdrop);
    font-family: "Arimo", Arial, sans-serif;
  }
  .letterhead {
    position: absolute;
    left: 90px;
    top: 20px;
    width: 820px;
    height: 1160px;
    background: var(--paper);
    overflow: hidden;
  }
  .brand {
    position: absolute;
    left: 40px;
    top: 68px;
    display: flex;
    align-items: center;
    gap: 12px;
  }
  .brand-mark {
    width: 52px;
    height: 52px;
    background: var(--brand-blue);
  }
  .brand-name {
    font-size: 26px;
    font-weight: 500;
    color: var(--brand-dark);
    letter-spacing: 0.3px;
    white-space: nowrap;
  }
  .contact {
    position: absolute;
    right: 72px;
    top: 80px;
    text-align: right;
    font-size: 19px;
    line-height: 24px;
    color: var(--ink);
    font-style: normal;
    white-space: nowrap;
  }
  .footer-rule {
    position: absolute;
    left: 0;
    right: 0;
    bottom: 40px;
    height: 6px;
    background: var(--rule-grey);
  }
  .footer-band {
    position: absolute;
    left: 0;
    right: 0;
    bottom: 0;
    height: 30px;
    background: var(--brand-blue);
  }
</style>
</head>
<body>
  <main class="letterhead">
    <header>
      <div class="brand">
        <span class="brand-mark"></span>
        <span class="brand-name">BKA Home Lending</span>
      </div>
      <address class="contact">
        203-481-7629<br>
        47 Fenbury Lane<br>
        Hollisford, CT 06412
      </address>
    </header>
    <footer>
      <div class="footer-rule"></div>
      <div class="footer-band"></div>
    </footer>
  </main>
</body>
</html>
```